Custom Manufacturing Job Shop

We are looking for a business card design for Tall Oak Fabrication Inc. Tall Oak is a family owned business that manufactures any custom product to fit a customers needs, whether it is custom 1 piece or production parts, we truly take on projects that others just cant do. to help in your design go to www.talloakfab.example for a more in depth idea. we have the following capabilities that we would like to see on the card somewhere...maybe on the back of a 2 sided card? we are fully open to ideas.
Machining
• Fabrication
• Millwork
• Maintenance
• Laser Cutting
• Precision Forming
Engineering
Blasting/Painting

No matter how big or small, We literally do it all

preferably black or darker cards but we don't mind to see some color if you see a better fit. we are interested in looking at anything that catches attention.
I have attached our logo, if it is needed in a different file type please let me know and I will send it to you if I can. maybe adding some type of drawing or dimensional lines would be something to add?? just throwing ideas out there....

Reason: I added one of our shredder designs and would like to see a few more cards if possible using this. any questions please don't hesitate to ask!!

Target Market(s)

anyone looking for design/manufacturing/machining whether it is custom 1 off parts or production.

Industry/Entity Type

Business

Contact Information for Business Card

preferably darker shades, but also not opposed to some color in the same sense....not too bright

Font styles to use
Serif
Sans Serif

Requirements
Must have
• Dell Marwick
• Direct:555-213-7790
• Cell:555-348-1162
• Fax: 555-907-4425
• 42 Quarry Lane
• Millbrook, ST 00000
• I also would request having it in a format I can give to the company making the business cards to edit names/numbers etc. for the entire staff.
Nice to have
• drafting lines? we are open to almost anything....
Should not have
• exotic colors

```html
<!DOCTYPE html>
<html lang="en">
<head>
<meta charset="utf-8">
<title>Tall Oak Fabrication Inc. – Stationery</title>
<link rel="stylesheet" href="https://fonts.googleapis.com/css2?family=Cinzel:wght@400;600&family=Open+Sans:wght@400;700&display=swap">
<style>
  :root{
    --bg:#e4e4e4;
    --ink:#3b3b3b;
    --ink-soft:#6a6a6a;
    --steel-dark:#3e3e3e;
    --steel-mid:#7c7c7c;
    --steel-light:#a9a9a9;
    --paper:#ffffff;
    --accent-red:#b3262b;
    --seal:#5fb6c9;
    --sign:#5a3f8f;
  }
  *{box-sizing:border-box;margin:0;padding:0}
  html,body{width:1200px;height:1200px;overflow:hidden}
  body{background:var(--bg);position:relative;font-family:"Open Sans",sans-serif;color:var(--ink)}

  .sheet{position:absolute;width:380px;height:537px;box-shadow:0 4px 14px rgba(0,0,0,.18)}
  .cover{left:200px;top:60px;background:linear-gradient(160deg,var(--steel-dark) 0%,#6b6b6b 55%,#9c9c9c 100%);border-bottom:3px solid var(--accent-red)}
  .letterhead{left:620px;top:60px;background:var(--paper)}

  .brand{font-family:"Open Sans",sans-serif;font-weight:700;letter-spacing:1px;line-height:1}
  .brand-web{font-size:8px;letter-spacing:1.5px;text-transform:uppercase}

  .cover .brand-block{position:absolute;top:82px;left:0;right:0;text-align:center;color:#e2e2e2}
  .cover .brand{font-size:28px}
  .cover .brand-web{margin-top:6px;color:#cfcfcf}

  .letterhead .brand-block{position:absolute;top:40px;right:0;left:0;text-align:center;color:var(--ink-soft)}
  .letterhead .brand{font-size:16px}
  .letterhead .brand-web{font-size:5px;margin-top:3px}

  .letter{position:absolute;left:38px;right:38px;top:126px;font-size:6.6px;line-height:1.5;color:#444}
  .letter p{margin-bottom:9px;text-align:justify}
  .letter .address{text-align:left}
  .signature{position:absolute;left:38px;top:392px;width:46px;height:22px;background:linear-gradient(90deg,rgba(90,63,143,.15),rgba(90,63,143,.35))}
  .seal{position:absolute;left:92px;top:384px;width:32px;height:32px;border-radius:50%;background:rgba(95,182,201,.35)}
  .letter-stripe{position:absolute;right:0;bottom:18px;width:160px;height:14px}

  .card{position:absolute;width:420px;height:240px;box-shadow:0 6px 16px rgba(0,0,0,.22);overflow:hidden}
  .card-front{left:140px;top:700px;background:linear-gradient(135deg,#ffffff 0%,#ececec 100%)}
  .card-back{left:640px;top:700px;background:linear-gradient(150deg,var(--steel-dark) 0%,#5a5a5a 100%)}

  .edge-strip{position:absolute;top:0;right:0;width:16px;height:100%}

  .card-front .brand-block{position:absolute;left:30px;top:88px;color:#4a4a4a}
  .card-front .brand{font-size:32px}
  .card-front .brand-web{margin-top:6px;color:var(--ink-soft)}
  .card-front .divider{position:absolute;left:30px;top:148px;width:160px;height:1px;background:#cfcfcf}
  .holder{position:absolute;right:38px;top:24px;text-align:right}
  .holder-name{font-family:"Cinzel",serif;font-weight:600;font-size:17px;color:var(--ink)}
  .holder-role{font-size:7px;letter-spacing:2px;color:var(--ink-soft);margin-top:2px}
  .contacts{position:absolute;right:38px;top:74px;list-style:none;font-size:8.5px;color:#555;text-align:right}
  .contacts li{display:flex;justify-content:flex-end;align-items:center;gap:6px;margin-bottom:4px}
  .contacts svg{width:9px;height:9px}
  .contacts .email{font-size:7.5px;letter-spacing:.6px;margin-top:3px}
  .address-block{position:absolute;left:30px;bottom:22px;font-family:"Cinzel",serif;font-size:8px;letter-spacing:.8px;line-height:1.5;color:#666}

  .card-back .brand-block{position:absolute;left:30px;top:96px;color:#dcdcdc}
  .card-back .brand{font-size:30px}
  .card-back .brand-web{margin-top:6px;color:#bdbdbd}
  .capabilities{position:absolute;left:218px;top:26px;list-style:none;font-family:"Cinzel",serif;font-size:12px;line-height:1.55;color:#f2f2f2;letter-spacing:.5px}
  .capabilities li::before{content:"•";margin-right:7px}
  .web-band{position:absolute;left:0;right:16px;bottom:0;height:30px;background:linear-gradient(90deg,#6f6f6f,#8d8d8d);font-family:"Cinzel",serif;font-size:9px;letter-spacing:2px;color:#f0f0f0;display:flex;align-items:center;justify-content:flex-end;padding-right:20px}
</style>
</head>
<body>

<section class="sheet cover" aria-label="Folder cover">
  <div class="brand-block">
    <div class="brand">TALL OAK</div>
    <div class="brand-web">talloakfab.example</div>
  </div>
</section>

<section class="sheet letterhead" aria-label="Letterhead">
  <div class="brand-block">
    <div class="brand">TALL OAK</div>
    <div class="brand-web">talloakfab.example</div>
  </div>
  <div class="letter">
    <p class="address">Jordan Avery<br>12 Harbour Rd<br>Perth, Australia</p>
    <p>Dear Jordan Avery,</p>
    <p>Thank you for your recent inquiry about our custom machining and fabrication services. Our team has reviewed your drawings and we are ready to quote both prototype and production runs at your convenience. Every part is inspected before it leaves our floor, and we keep records for each job we ship.</p>
    <p>We handle laser cutting, precision forming, millwork and finishing under one roof, so your parts stay on schedule from first cut to final coat. Our engineers can also help refine your design for easier and lower cost manufacturing.</p>
    <p>Please find our proposal enclosed. Call us with any questions and we will gladly walk you through each step of the process.</p>
    <p class="address">Yours Sincerely,<br>Aaron Pell.</p>
  </div>
  <div class="signature" role="img" aria-label="Handwritten signature"></div>
  <div class="seal" role="img" aria-label="Company seal"></div>
  <svg class="letter-stripe" viewBox="0 0 160 14" aria-hidden="true">
    <polygon points="0,14 10,0 18,0 8,14" fill="#7a7a7a"/>
    <polygon points="14,14 24,0 32,0 22,14" fill="#7a7a7a"/>
    <polygon points="30,14 40,0 160,0 160,14" fill="#5a5a5a"/>
  </svg>
</section>

<section class="card card-front" aria-label="Business card front">
  <div class="brand-block">
    <div class="brand">TALL OAK</div>
    <div class="brand-web">talloakfab.example</div>
  </div>
  <div class="divider"></div>
  <div class="holder">
    <div class="holder-name">Dell Marwick</div>
    <div class="holder-role">DIRECT</div>
  </div>
  <ul class="contacts">
    <li>555-213-7790<svg viewBox="0 0 10 10" aria-hidden="true"><path d="M2 1h2l1 2-1.2 1a5 5 0 0 0 2.2 2.2L7 5l2 1v2c0 .6-.4 1-1 1A8 8 0 0 1 1 2c0-.6.4-1 1-1z" fill="#555"/></svg></li>
    <li>555-348-1162<svg viewBox="0 0 10 10" aria-hidden="true"><rect x="2.5" y=".5" width="5" height="9" rx="1" fill="#555"/><rect x="3.4" y="1.6" width="3.2" height="5.6" fill="#eee"/></svg></li>
    <li>555-907-4425<svg viewBox="0 0 10 10" aria-hidden="true"><rect x="1" y="4" width="8" height="5" rx="1" fill="#555"/><rect x="3" y="1" width="4" height="3.5" fill="#555"/></svg></li>
    <li class="email">INFO@TALLOAKFAB.EXAMPLE</li>
  </ul>
  <div class="address-block">42 Quarry Lane<br>Millbrook, ST 00000</div>
  <svg class="edge-strip" viewBox="0 0 16 240" preserveAspectRatio="none" aria-hidden="true">
    <rect width="16" height="240" fill="#8a8a8a"/>
    <polygon points="0,40 16,28 16,34 0,46" fill="#ffffff"/>
    <polygon points="0,52 16,40 16,46 0,58" fill="#ffffff"/>
  </svg>
</section>

<section class="card card-back" aria-label="Business card back">
  <div class="brand-block">
    <div class="brand">TALL OAK</div>
    <div class="brand-web">talloakfab.example</div>
  </div>
  <ul class="capabilities">
    <li>Machining</li>
    <li>Fabrication</li>
    <li>Millwork</li>
    <li>Maintenance</li>
    <li>Laser Cutting</li>
    <li>Precision Forming</li>
    <li>Engineering</li>
    <li>Blasting/Painting</li>
  </ul>
  <div class="web-band">WWW.TALLOAKFAB.EXAMPLE</div>
  <svg class="edge-strip" viewBox="0 0 16 240" preserveAspectRatio="none" aria-hidden="true">
    <rect width="16" height="240" fill="#b5b5b5"/>
  </svg>
</section>

</body>
</html>
```